WEb page design for the nations most eco friendly hair salon. Need to be able to link on online salo

Torvan Eco Salon, will be the nations most eco friendly hair salon. Opening In Jacksonville Beach, Florida in December 2015. This will be the first salon in the nation and potentially the world to be, 100% solar powered. eliminating plastics usage by 99%. chemical and ammonia free color, non toxic paint, non vinyl furniture. 99% recycling procedures in place including, all aluminum, cardboard, batteries, lighbulbs, hair clippings, etc...thanks to our partnership with Blue Meadow Studios. This will be a salon where Simplicity and luxury can finally coexist in perfect harmony. We will not only completely eliminate the threat of any future damage done to our planet from this point forward, but we will strive every day to reduce as much damage that has been done by taking every effort necessary to showcase a more beautiful way to take care of the earth and ourselves.

Target Market(s)

middle aged business men and women.

Industry/Entity Type

Hair And Beauty

Coding

Coded - Design and coding required

Number of Pages Required

2 page

Colors
000000

Requirements
Must have
• link to salon online booking software, and maximum 2 charitable foundations that our salon will be involved with as well as instagram and facebook page.
• hours of operation 10am-8pm Monday-Friday
• 10am-6pm Saturdays
Nice to have
• Lumora hair care products
• address 817 lower n 6th st Jacksonville beach fl, 32075
• email lumorastudio@mailvento.net

```html
<!DOCTYPE html>
<html lang="en">
<head>
<meta charset="utf-8">
<title>Torvan Eco Salon</title>
<link rel="stylesheet" href="https://fonts.googleapis.com/css2?family=Dosis:wght@300;400;600&family=Open+Sans:wght@300;400&family=Ubuntu:wght@300;400;500&display=swap">
<style>
  :root {
    --green: #3d9f3d;
    --green-soft: #5aaf5a;
    --blue: #3a6fc4;
    --brand: #7f8fc6;
    --text: #555a60;
    --muted: #8a8f95;
    --light: #b3b6ba;
    --white: #ffffff;
    --hero-top: #7aa3b4;
    --hero-mid: #8a9fac;
    --hero-low: #55687a;
  }
  * { box-sizing: border-box; margin: 0; padding: 0; }
  html, body { width: 768px; height: 1200px; overflow: hidden; background: var(--white); }
  body { font-family: "Ubuntu", sans-serif; color: var(--text); position: relative; }
  .wrap { width: 482px; margin: 0 auto; position: relative; }

  .site-header { height: 58px; }
  .site-header .wrap { height: 58px; display: flex; align-items: center; justify-content: space-between; }
  .brand { font-family: "Dosis", sans-serif; font-weight: 600; font-size: 17px; color: var(--brand); display: flex; align-items: center; gap: 6px; letter-spacing: .3px; }
  .brand-dot { width: 10px; height: 10px; background: var(--brand); border-radius: 50%; }
  .main-nav { display: flex; align-items: center; gap: 18px; font-size: 8px; color: var(--muted); font-weight: 300; }
  .btn-outline { border: 1px solid var(--blue); color: var(--blue); border-radius: 3px; padding: 7px 16px; font-size: 8px; margin-left: 8px; letter-spacing: .3px; }

  .hero { height: 320px; position: relative; background: linear-gradient(180deg, var(--hero-top) 0%, var(--hero-mid) 42%, var(--hero-low) 100%); display: flex; flex-direction: column; align-items: center; color: var(--white); text-align: center; }
  .hero-lead { font-family: "Dosis", sans-serif; font-weight: 300; font-size: 29px; line-height: 41px; margin-top: 128px; }
  .hero-strong { font-family: "Dosis", sans-serif; font-weight: 600; font-size: 25px; margin-top: 5px; }

  .features { text-align: center; padding-top: 40px; }
  .section-title { font-family: "Dosis", sans-serif; font-weight: 300; font-size: 21px; color: var(--text); }
  .feature-grid { display: grid; grid-template-columns: repeat(3, 1fr); row-gap: 46px; margin-top: 40px; }
  .feature { display: flex; flex-direction: column; align-items: center; }
  .feature svg { width: 32px; height: 32px; }
  .feature p { color: var(--green-soft); font-size: 10px; line-height: 14px; margin-top: 10px; }
  .more-link { display: inline-block; margin-top: 42px; color: var(--green-soft); font-family: "Dosis", sans-serif; font-weight: 300; font-size: 11px; }

  .cta { position: absolute; top: 763px; left: 0; width: 768px; height: 226px; background: linear-gradient(110deg, #6f8796 0%, #8aa3ad 45%, #a9bcc2 70%, #94aebb 100%); }
  .cta .wrap { height: 226px; display: flex; align-items: center; justify-content: space-between; color: var(--white); }
  .cta-title { font-family: "Dosis", sans-serif; font-weight: 600; font-size: 23px; line-height: 28px; }
  .cta-sub { font-family: "Dosis", sans-serif; font-weight: 300; font-size: 28px; line-height: 34px; }
  .btn-solid { background: var(--white); color: #6d747a; font-family: "Dosis", sans-serif; font-weight: 600; font-size: 12px; letter-spacing: .6px; padding: 13px 22px; border-radius: 2px; }

  .site-footer { position: absolute; top: 1031px; left: 0; width: 768px; }
  .footer-grid { display: flex; justify-content: space-between; }
  .footer-brand { color: #9a9da1; font-size: 16px; margin-top: 8px; }
  .footer-links { display: flex; gap: 25px; margin-top: 55px; font-size: 8px; font-weight: 500; color: #4b5055; letter-spacing: .3px; }
  .hours { width: 214px; font-family: "Open Sans", sans-serif; }
  .hours-title { font-size: 13px; color: #4b5055; display: flex; align-items: center; gap: 10px; }
  .status { width: 9px; height: 9px; border-radius: 50%; background: #d8eed8; display: flex; align-items: center; justify-content: center; }
  .status::after { content: ""; width: 5px; height: 5px; border-radius: 50%; background: var(--green); }
  .hours-cols { display: flex; justify-content: space-between; margin-top: 18px; }
  .hours-day { font-size: 10px; color: #4b5055; }
  .hours-time { font-size: 17px; font-weight: 300; color: #6a6f74; margin-top: 4px; }
  .footer-base { display: flex; justify-content: space-between; align-items: center; margin-top: 30px; }
  .copyright { font-size: 7px; color: var(--light); font-weight: 300; }
  .social { display: flex; gap: 10px; }
  .social span { width: 10px; height: 10px; border-radius: 50%; background: var(--light); }
</style>
</head>
<body>
  <header class="site-header">
    <div class="wrap">
      <div class="brand"><span class="brand-dot"></span>Torvan Eco Salon</div>
      <nav class="main-nav">
        <span>Why us?</span><span>About us</span><span>Prices</span><span>Contact us</span>
        <span class="btn-outline">BOOK NOW</span>
      </nav>
    </div>
  </header>

  <section class="hero" role="img" aria-label="Photo of a person meditating in a desert valley at sunrise">
    <p class="hero-lead">Leading the industry with an innovative<br>new approach in luxury hair care.</p>
    <p class="hero-strong">A fully solar powered, eco-concious salon.</p>
  </section>

  <section class="features">
    <div class="wrap">
      <h2 class="section-title">Our features</h2>
      <div class="feature-grid">
        <div class="feature">
          <svg viewBox="0 0 32 32" aria-hidden="true"><rect x="4" y="2" width="2" height="4" fill="var(--green)"/><rect x="9" y="2" width="2" height="4" fill="var(--green)"/><rect x="2" y="6" width="11" height="7" rx="1" fill="var(--green)"/><path d="M7 13 V18 H13" stroke="var(--green)" stroke-width="2" fill="none"/><circle cx="21" cy="21" r="6" fill="var(--green)"/><g stroke="var(--green)" stroke-width="1.5"><line x1="21" y1="11" x2="21" y2="13"/><line x1="21" y1="29" x2="21" y2="31"/><line x1="11" y1="21" x2="13" y2="21"/><line x1="29" y1="21" x2="31" y2="21"/></g></svg>
          <p>100% solar powered</p>
        </div>
        <div class="feature">
          <svg viewBox="0 0 32 32" aria-hidden="true"><g transform="rotate(-40 16 16)"><rect x="4" y="9" width="24" height="7" rx="3.5" fill="var(--green)"/><rect x="4" y="17" width="24" height="7" rx="3.5" fill="var(--green)"/></g><circle cx="9" cy="23" r="2" fill="#fff"/><circle cx="13" cy="27" r="2" fill="#fff"/></svg>
          <p>Biodegradable towels</p>
        </div>
        <div class="feature">
          <svg viewBox="0 0 32 32" aria-hidden="true"><path d="M24 2 L30 8 L11 27 L3 29 L5 21Z" fill="var(--green)"/><path d="M22 6 L26 10 L10 26 L6 22Z" fill="#fff"/><path d="M23 7 L25 9 L10 24 L8 22Z" fill="var(--green)"/></svg>
          <p>100% Natural<br>and LED lighting</p>
        </div>
        <div class="feature">
          <svg viewBox="0 0 32 32" aria-hidden="true"><path d="M16 4 L16 20 L9 20Z" fill="var(--green)"/><path d="M17 6 L23 20 L17 20Z" fill="var(--green)"/><path d="M3 22 H29 L25 28 H7Z" fill="var(--green)"/></svg>
          <p>Produces printed<br>with no toxic ink</p>
        </div>
        <div class="feature">
          <svg viewBox="0 0 32 32" aria-hidden="true"><path d="M8 2 H27 V27 H8Z" fill="none" stroke="var(--green)" stroke-width="1.5"/><path d="M4 27 H23 V30 H4Z" fill="none" stroke="var(--green)" stroke-width="1.5"/><line x1="27" y1="2" x2="27" y2="5" stroke="var(--green)" stroke-width="1.5"/></svg>
          <p>Recycled foils</p>
        </div>
        <div class="feature">
          <svg viewBox="0 0 32 32" aria-hidden="true"><rect x="1" y="3" width="30" height="12" rx="1" fill="var(--green)"/><rect x="4" y="7" width="5" height="2" fill="#fff"/><path d="M20 8 H25 V22 H22 V11 H20Z" fill="#fff"/><g stroke="var(--green)" stroke-width="1.5"><line x1="20" y1="23" x2="18" y2="29"/><line x1="23" y1="23" x2="21" y2="29"/><line x1="26" y1="23" x2="24" y2="29"/></g></svg>
          <p>Automatic lights<br>and hand dryers</p>
        </div>
      </div>
      <span class="more-link">Watch more features &nbsp;›</span>
    </div>
  </section>

  <section class="cta" role="img" aria-label="Photo of a rocky canyon under a blue sky">
    <div class="wrap">
      <div>
        <p class="cta-title">Book your visit now!</p>
        <p class="cta-sub">Save the nature ,live better!</p>
      </div>
      <span class="btn-solid">BOOK NOW</span>
    </div>
  </section>

  <footer class="site-footer">
    <div class="wrap">
      <div class="footer-grid">
        <div>
          <div class="brand footer-brand">Torvan Eco Salon</div>
          <div class="footer-links"><span>BANNER HERE</span><span>BANNER HERE</span></div>
        </div>
        <div class="hours">
          <div class="hours-title">Opening Hours <span class="status"></span></div>
          <div class="hours-cols">
            <div><p class="hours-day">Mon - Fri</p><p class="hours-time">9:00 - 22:00</p></div>
            <div><p class="hours-day">Sat - Sun</p><p class="hours-time">10:00 - 23:00</p></div>
          </div>
        </div>
      </div>
      <div class="footer-base">
        <p class="copyright">© 2015 All Rights Reserved.</p>
        <div class="social" aria-label="Social links"><span></span><span></span><span></span></div>
      </div>
    </div>
  </footer>
</body>
</html>
```